"Orvana" - Ketamine Clinic - Save Minds and Heal Hearts!! -

I need a very nice modern happy brain themed warm website design for our cutting edge modern and caring ketamine IV infusion clinic that also offers talk therapy and telemedicine visits.
A great design using the color schemes in out logos (grey, white, purples and that need metallic fading colored effect in the logo).

```html
<!DOCTYPE html>
<html lang="en">
<head>
<meta charset="utf-8">
<title>Orvana – Ketamine Clinic</title>
<link href="https://fonts.googleapis.com/css2?family=Roboto:wght@400;500;700&display=swap" rel="stylesheet">
<style>
:root{
  --purple:#4a06a6;
  --purple-deep:#3b0595;
  --ink:#111;
  --text:#222;
  --white:#fff;
  --card:rgba(205,205,212,.88);
  --footer-top:#9a9a9a;
  --footer-bottom:#6a6a6a;
  --bar:#3d3d3d;
}
*{margin:0;padding:0;box-sizing:border-box}
html,body{width:837px;height:1200px;overflow:hidden;background:var(--white)}
body{position:relative;font-family:"Roboto",Arial,sans-serif;color:var(--text)}
a{color:inherit;text-decoration:none}
.abs{position:absolute}

.topbar{left:0;top:0;width:837px;height:19px;background:var(--purple);color:var(--white);font-size:7.5px;font-weight:700}
.topbar .contact{left:84px;top:5px;display:flex;gap:12px;align-items:center}
.topbar .contact span{display:flex;align-items:center;gap:5px}
.topbar .services{right:84px;top:5px;display:flex;gap:11px}

.header{left:0;top:19px;width:837px;height:83px;background:var(--white)}
.nav{top:38px;display:flex;gap:17px;font-size:10px;font-weight:500;letter-spacing:1.3px;color:var(--ink)}
.nav.left{left:153px}
.nav.right{left:497px}
.nav .current{color:var(--purple)}
.brand{left:410px;top:24px;display:flex;align-items:center;gap:4px;font-size:20px;font-weight:700;color:var(--purple)}
.brand .dot{width:10px;height:10px;border-radius:50%;background:var(--purple)}
.search{left:673px;top:38px}

.hero{left:0;top:102px;width:837px;height:372px;background:radial-gradient(ellipse at 30% 30%,#2f3fd0 0%,#14207a 30%,#070c30 60%),linear-gradient(180deg,#0a1848 0%,#0b0f2e 55%,#8a1650 100%);background-blend-mode:screen}
.hero-card{left:484px;top:140px;width:263px;height:295px;background:var(--card);padding:80px 24px 0 24px}
.hero-card h1{font-size:15.5px;line-height:24px;font-weight:700;color:var(--purple)}
.hero-card p{margin-top:8px;font-size:10.5px;line-height:20px;color:var(--ink)}
.btn-book{display:inline-block;margin:10px 0 0 6px;background:var(--purple);color:var(--white);font-size:8.5px;padding:8px 18px}

.welcome{left:0;top:530px;width:837px;text-align:center}
.welcome h2{font-size:25px;font-weight:700;color:var(--purple)}
.welcome h3{margin-top:22px;font-size:21px;font-weight:500;color:var(--ink)}

.about-ring{left:161px;top:657px;width:236px;height:236px;border-radius:50%;border:3px solid var(--purple);border-left-color:transparent;border-bottom-color:transparent;transform:rotate(10deg)}
.about-photo{left:163px;top:660px;width:232px;height:222px;border-radius:50%;background:radial-gradient(circle at 50% 35%,#e8d9c4 0%,#b58c6b 45%,#4d4352 100%)}
.about{left:437px;top:662px;width:300px}
.about h2{font-size:19px;font-weight:700;color:var(--purple)}
.about p{margin-top:10px;font-size:9.5px;line-height:18px;color:var(--ink)}
.btn-learn{display:inline-flex;align-items:center;gap:5px;margin-top:22px;background:var(--purple);color:var(--white);font-size:11px;padding:8px 12px;border-radius:14px}

.footer{left:0;top:935px;width:837px;height:227px;background:linear-gradient(180deg,var(--footer-top),var(--footer-bottom))}
.footer-brand{left:110px;top:1035px;display:flex;align-items:center;gap:5px;font-size:26px;font-weight:700;color:var(--white)}
.footer-brand .dot{width:14px;height:14px;border-radius:50%;background:var(--white)}
.fcol{top:980px;color:var(--white);font-size:10px}
.fcol h4{font-size:12.5px;font-weight:500;color:var(--purple);margin-bottom:12px}
.fcol li{list-style:none;margin-bottom:9.5px}
.fcol li::before{content:"•";margin-right:4px}
.fcol .row{display:flex;align-items:center;gap:8px;margin-bottom:7px}
.fcol .label{font-weight:700;margin:14px 0 12px}
.fcol .addr{line-height:19px}

.bottombar{left:0;top:1162px;width:837px;height:38px;background:var(--bar);color:var(--white);font-size:10px}
.bottombar .copy{left:84px;top:13px}
.social{right:84px;top:12px;display:flex;gap:14px}
.social span{width:14px;height:14px;border-radius:50%;background:var(--white)}
</style>
</head>
<body>

<div class="abs topbar">
  <div class="abs contact">
    <span><svg width="7" height="7" viewBox="0 0 10 10"><path d="M2 0l2 2.5-1.2 1.3c.6 1.4 1.6 2.4 3 3L7 5.6 9.5 7.6 8.5 9.5C4 9.5.5 6 .5 1.5z" fill="#fff"/></svg>+1 555 0142</span>
    <span><svg width="8" height="6" viewBox="0 0 10 7"><rect width="10" height="7" fill="#fff"/><path d="M0 0l5 4 5-4" fill="none" stroke="#4a06a6"/></svg>hello@orvana.com</span>
  </div>
  <div class="abs services"><span>Ketamine Infusion Therapy</span><span>Talk Therapy</span><span>Telemedicine Visits</span></div>
</div>

<header class="abs header"></header>
<nav class="abs nav left"><a class="current">Home</a><a>About Orvana</a><a>Orvana Services ⌄</a></nav>
<div class="abs brand"><span class="dot"></span>Orvana</div>
<nav class="abs nav right"><a>FAQ’s</a><a>Blog</a><a>Contact Us</a></nav>
<svg class="abs search" width="11" height="11" viewBox="0 0 12 12"><circle cx="7" cy="5" r="4" fill="none" stroke="#222" stroke-width="1.2"/><path d="M4 8L1 11" stroke="#222" stroke-width="1.2"/></svg>

<section class="abs hero" role="img" aria-label="Glowing blue brain floating above an open hand on a dark floral background"></section>
<div class="abs hero-card">
  <h1>"Orvana" - Ketamine Clinic Save Minds and Heal Hearts!!</h1>
  <p>Modern and caring ketamine IV infusion clinic that also offers talk therapy and telemedicine visits.</p>
  <a class="btn-book">Book Now</a>
</div>

<section class="abs welcome">
  <h2>Welcome to “Orvana” – Ketamine Clinic</h2>
  <h3>Save Minds and Heal Hearts</h3>
</section>

<div class="abs about-ring"></div>
<div class="abs about-photo" role="img" aria-label="Group of smiling young friends taking a selfie outdoors"></div>
<section class="abs about">
  <h2>About Orvana</h2>
  <p>Modern and caring ketamine IV infusion clinic that also offers talk therapy and telemedicine visits.</p>
  <p>Modern and caring ketamine IV infusion clinic that also offers talk therapy and telemedicine visits.</p>
  <p>Modern and caring ketamine IV infusion clinic that also offers talk therapy and telemedicine visits.</p>
  <a class="btn-learn">Learn More <svg width="11" height="11" viewBox="0 0 12 12"><circle cx="6" cy="6" r="5" fill="none" stroke="#fff"/><path d="M5 3.5L7.5 6 5 8.5" fill="none" stroke="#fff"/></svg></a>
</section>

<footer class="abs footer"></footer>
<div class="abs footer-brand"><span class="dot"></span>Orvana</div>
<div class="abs fcol" style="left:260px">
  <h4>Quick Links</h4>
  <ul><li>About Orvana</li><li>Orvana Services</li><li>FAQ’s</li><li>Blog</li><li>Contact Us</li></ul>
</div>
<div class="abs fcol" style="left:437px">
  <h4>Orvana Services</h4>
  <ul><li>Ketamine Infusion Therapy</li><li>Talk Therapy</li><li>Telemedicine Visits</li></ul>
</div>
<div class="abs fcol" style="left:613px">
  <h4>Get In Touch</h4>
  <div class="row"><svg width="9" height="9" viewBox="0 0 10 10"><path d="M2 0l2 2.5-1.2 1.3c.6 1.4 1.6 2.4 3 3L7 5.6 9.5 7.6 8.5 9.5C4 9.5.5 6 .5 1.5z" fill="#fff"/></svg>+1 555 0142</div>
  <div class="row"><svg width="10" height="7" viewBox="0 0 10 7"><rect width="10" height="7" fill="#fff"/><path d="M0 0l5 4 5-4" fill="none" stroke="#7a7a7a"/></svg>hello@orvana.com</div>
  <div class="label">Address :</div>
  <div class="addr">240 Willow Ave, Suite B,<br>Austin, Texas, USA</div>
</div>

<div class="abs bottombar">
  <div class="abs copy">Copyright © 2023 "Orvana". - Ketamine Clinic</div>
  <div class="abs social"><span></span><span></span><span></span></div>
</div>

</body>
</html>
```